Take my 1-Page Consulting Service Introduction to the next level!

I am looking for a designer to enhance my current 1-Page Consulting Services Introduction.

My business - Bright Harbor Advisory - offers HR consulting to companies looking to be more people-centric. The design should be professional, but also convey a sense of "sparking people" or inspiring people to engage and excel.

The new Word document will:
* Use my new business logo, logo icon and colors. (files attached)
* Include my head shot (file attached)
* Impress potential clients by improving the visual appeal
* Be easy for me to update in Word (small edits)

Target Market(s)

Business owners and senior leaders

Font styles to use
Sans Serif

Requirements
Must have
• My head shot (can be cropped) , my logo
Nice to have
• use of my logo icon or parts of it (if that works for the design)

```html
<!DOCTYPE html>
<html lang="en">
<head>
<meta charset="utf-8">
<title>Dana Whitlow – Bright Harbor Advisory</title>
<link rel="stylesheet" href="https://fonts.googleapis.com/css2?family=Lato:wght@400;700;900&display=swap">
<style>
  :root {
    --brand-blue: #1f5a96;
    --brand-blue-dark: #174878;
    --ink: #3a3a3a;
    --paper: #ffffff;
    --backdrop: #d8d8d8;
    --photo-light: #c9c9c9;
    --photo-dark: #6f6f6f;
    --rule: #9aa3ad;
  }
  * { box-sizing: border-box; margin: 0; padding: 0; }
  html, body {
    width: 1200px; height: 877px; overflow: hidden;
    background: var(--backdrop);
    font-family: "Lato", Arial, sans-serif;
    color: var(--ink);
  }
  .sheet {
    position: absolute; left: 300px; top: 50px;
    width: 600px; height: 776px;
    background: var(--paper);
    box-shadow: 0 6px 18px rgba(0,0,0,.18);
    overflow: hidden;
  }
  .side-panel { position: absolute; left: 0; top: 0; width: 600px; height: 776px; }
  .profile-name {
    position: absolute; left: 0; top: 84px; width: 285px;
    text-align: center; color: var(--paper);
    font-size: 30px; font-weight: 700; letter-spacing: .2px;
  }
  .headshot {
    position: absolute; left: 46px; top: 132px;
    width: 192px; height: 192px; border-radius: 50%;
    border: 4px solid var(--paper);
    background: radial-gradient(circle at 50% 40%, var(--photo-light), var(--photo-dark));
  }
  .services {
    position: absolute; left: 40px; top: 360px; width: 230px;
    list-style: none; color: var(--paper); font-size: 12px; line-height: 14px;
  }
  .services li { position: relative; padding-left: 18px; margin-bottom: 9px; }
  .services li::before {
    content: ""; position: absolute; left: 0; top: 5px;
    width: 4px; height: 4px; border-radius: 50%; background: var(--paper);
  }
  .brand {
    position: absolute; left: 305px; top: 24px; width: 270px;
    display: flex; align-items: center; justify-content: center; gap: 7px;
    color: var(--brand-blue); font-weight: 900; font-size: 17px;
  }
  .brand-dot { width: 12px; height: 12px; border-radius: 50%; background: var(--brand-blue); }
  .main-column { position: absolute; left: 305px; top: 72px; width: 272px; font-size: 10px; line-height: 1.42; }
  .contact { color: var(--brand-blue); font-weight: 700; font-size: 10.5px; margin-bottom: 8px; }
  .bio { margin-bottom: 10px; }
  .section-title { color: var(--brand-blue); font-weight: 900; font-size: 16px; margin: 16px 0 6px; }
  .experience { list-style: none; margin-bottom: 14px; }
  .experience li { position: relative; padding-left: 12px; margin-bottom: 1px; }
  .experience li::before {
    content: ""; position: absolute; left: 1px; top: 6px;
    width: 3px; height: 3px; border-radius: 50%; background: var(--ink);
  }
  .impact {
    position: absolute; left: 0; top: 702px; width: 600px; height: 74px;
    display: flex; align-items: center; padding: 0 20px;
  }
  .impact-tag { position: relative; width: 96px; height: 40px; flex: none; margin-right: 14px; }
  .impact-tag svg { position: absolute; inset: 0; }
  .impact-tag span {
    position: relative; display: block; line-height: 40px; padding-left: 14px;
    color: var(--paper); font-weight: 900; font-size: 11px; letter-spacing: .5px;
  }
  .impact-points { display: flex; flex: 1; }
  .impact-point {
    flex: 1; padding: 0 12px; font-size: 10px; line-height: 1.4;
    border-left: 1px solid var(--rule);
  }
  .impact-point:first-child { border-left: none; }
</style>
</head>
<body>
  <article class="sheet">
    <svg class="side-panel" viewBox="0 0 600 776" aria-hidden="true">
      <polygon points="0,52 285,52 285,620 0,698" fill="var(--brand-blue)"/>
    </svg>

    <h1 class="profile-name">Dana Whitlow</h1>
    <div class="headshot" role="img" aria-label="Head shot of the consultant"></div>

    <ul class="services">
      <li>People Strategies &amp; Execution</li>
      <li>Business Transformation</li>
      <li>Change Leadership</li>
      <li>People Systems</li>
      <li>Leadership Development</li>
      <li>Personal &amp; Team Effectiveness</li>
      <li>Coaching</li>
      <li>Employee Engagement</li>
      <li>Learning &amp; Development</li>
      <li>People-Centric Outsourcing</li>
    </ul>

    <div class="brand"><span class="brand-dot"></span><span>Bright Harbor Advisory</span></div>

    <section class="main-column">
      <p class="contact">Vancouver, BC Canada | 604.555.0142 |<br>dwhitlow@brightharbor.com |</p>
      <p class="bio">Dana provides people strategy expertise that enables business growth and success. She’s known for change, learning, culture and performance systems that engage and empower. Dana partners with boards and leadership teams to convert vision into action and thrives on kick-starting business initiatives. She is a champion of people-centric decision-making with a wide range of industry experience.</p>
      <p class="bio">Dana fosters cultures that create meaningful in-person, hybrid and virtual team connection. She has dual US and Canadian citizenship and works cross-border with ease. www.linkedin.com/in/danawhitlow</p>

      <h2 class="section-title">Professional Experience</h2>
      <ul class="experience">
        <li>Vice President, Development &amp; Culture/Learning Cedarline Building Solutions</li>
        <li>Director Restaurant Training &amp; Transformation Maple Grill Food Services of Canada</li>
        <li>Director of Education Pacific Realty Association</li>
        <li>Head of Virtual Communities Global Diploma Board</li>
        <li>Director of Academic Technology Services Ridgeline College</li>
      </ul>
      <p>Dana holds a Masters of Arts in Education and Human Development. She is a certified Clearview personal effectiveness coach, a certified Talentscope Assessments coach and an experienced ChangeWorks Certified Change Practitioner.</p>
    </section>

    <section class="impact">
      <div class="impact-tag">
        <svg viewBox="0 0 96 40" aria-hidden="true"><polygon points="0,0 78,0 96,20 78,40 0,40" fill="var(--brand-blue)"/></svg>
        <span>IMPACT</span>
      </div>
      <div class="impact-points">
        <p class="impact-point">Creating people strategies that engage, inspire and enable organizational growth and success.</p>
        <p class="impact-point">Creating people strategies that engage, inspire and enable organizational growth and success.</p>
        <p class="impact-point">Creating people strategies that engage, inspire and enable organizational growth and success.</p>
      </div>
    </section>
  </article>
</body>
</html>
```